Brenmoor Group needs a business card

I would like the card to be simple but modern and elegant.
I like black and white.
or black and gold.
we are a private finance lender and also are involved in property and property developments.

please look at the business card photos i provided i would like B.G only one one side and all the other details on the other side use fonts that tie in with my theme.

Industry/Entity Type

Finance

Contact Information for Business Card

Brenmoor Group (B.G) Callum Brenmoor M: 0418396152 E: callumbren@quivomail.com

Font styles to use
Other font styles liked:
• Use fonts that would reflect our business

Colors
000000
ffffff

Requirements
Must have
• one side of details
• other side has either B.G or Brenmoor Group like in the photos provided

```html
<!DOCTYPE html>
<html lang="en">
<head>
<meta charset="utf-8">
<title>Brenmoor Group — Business Card</title>
<link rel="stylesheet" href="https://fonts.googleapis.com/css2?family=Montserrat:wght@500;600;700&display=swap">
<style>
  :root {
    --backdrop: #3a3a3a;
    --card-black: #0d0d0d;
    --gold: #c9a553;
    --gold-soft: #b8954a;
  }
  * { margin: 0; padding: 0; box-sizing: border-box; }
  html, body {
    width: 1200px;
    height: 900px;
    overflow: hidden;
    background: var(--backdrop);
  }
  .canvas {
    position: relative;
    width: 1200px;
    height: 900px;
    font-family: "Montserrat", sans-serif;
  }
  .card {
    position: absolute;
    width: 630px;
    height: 360px;
    background: var(--card-black);
    box-shadow: 0 10px 28px rgba(0,0,0,0.45);
  }
  .card--details { left: 480px; top: 50px; }
  .card--brand { left: 90px; top: 480px; }

  .company {
    position: absolute;
    left: 58px;
    top: 150px;
    display: flex;
    align-items: center;
    gap: 12px;
    color: var(--gold);
    font-weight: 600;
    font-size: 19px;
    letter-spacing: 0.3px;
  }
  .company__mark {
    width: 12px;
    height: 12px;
    background: var(--gold);
  }
  .holder-name {
    position: absolute;
    left: 368px;
    top: 62px;
    color: var(--gold);
    font-weight: 700;
    font-size: 15px;
    letter-spacing: 1.4px;
    text-transform: uppercase;
  }
  .contact {
    position: absolute;
    left: 400px;
    top: 192px;
    list-style: none;
    color: var(--gold-soft);
    font-weight: 500;
    font-size: 13.5px;
    line-height: 20px;
    letter-spacing: 0.6px;
  }
  .brand-initials {
    position: absolute;
    left: 0;
    right: 0;
    top: 50%;
    transform: translateY(-50%);
    text-align: center;
    color: var(--gold);
    font-weight: 700;
    font-size: 64px;
    letter-spacing: 2px;
  }
</style>
</head>
<body>
  <main class="canvas">
    <section class="card card--details" aria-label="Card front with contact details">
      <div class="company">
        <span class="company__mark" aria-hidden="true"></span>
        <span class="company__name">Brenmoor Group</span>
      </div>
      <p class="holder-name">Callum Brenmoor</p>
      <ul class="contact">
        <li class="contact__phone">M: 0418396152</li>
        <li class="contact__email">E: callumbren@quivomail.com</li>
      </ul>
    </section>

    <section class="card card--brand" aria-label="Card back with brand initials">
      <p class="brand-initials">B.G</p>
    </section>
  </main>
</body>
</html>
```